IT Company that provides secure IT solutions and services to our customers

We need business cards and a logo for a new IT Solutions company just created based in Kuala Lumpur, Malaysia. But will also be serving other countries in the region. We provide secure data, voice solutions on mobile platforms. Our first offering is encrypted voice and data solutions for ZUN, Pellovan, Quillet and Frondmoss devices.

Target Market(s)

large organizations Govt, Police, Defence, Anti-corruption, Legal, highly regulated industries such as Health-care, Financial, Banking, Insurance,

Industry/Entity Type

Information Technology

Contact Information for Business Card

VorlexIT (Logo - colour is ORVA blue)Rashid Nawfal Managing Director Vorlex IT Sdn. Bhd.3rd Floor, Block C, Wisma LPN,No.14 Jalan Seri Hamzani,58410, Kuala LumpurMalaysia

Font styles to use
Sans Serif

Colors
3176b5
ec1f27
fbed22

Requirements
Must have
• VorlexIT all in Blue like ORVA blue. A logo design perhaps a play of VI, K with a dangling T (colour can be any)
Nice to have
• I want a clean crisp card, not too busy, easy to read.

```html
<!DOCTYPE html>
<html lang="en">
<head>
<meta charset="utf-8">
<title>VorlexIT Business Cards</title>
<link rel="stylesheet" href="https://fonts.googleapis.com/css2?family=Open+Sans:wght@400;600;700&family=PT+Sans+Narrow:wght@700&display=swap">
<style>
  :root {
    --brand-blue: #1e5fae;
    --brand-red: #d8232a;
    --card-white: #ffffff;
    --backdrop: #e9e6e3;
    --text-light: #ffffff;
  }
  * { margin: 0; padding: 0; box-sizing: border-box; }
  html, body {
    width: 1200px;
    height: 900px;
    overflow: hidden;
    background: var(--backdrop);
  }
  .canvas {
    position: relative;
    width: 1200px;
    height: 900px;
  }
  .card {
    position: absolute;
    background: var(--card-white);
    overflow: hidden;
    box-shadow: 0 6px 18px rgba(0, 0, 0, 0.12);
  }
  .card--front { left: 238px; top: 62px; width: 555px; height: 343px; }
  .card--back  { left: 457px; top: 518px; width: 560px; height: 344px; }

  .card__bands {
    position: absolute;
    inset: 0;
    width: 100%;
    height: 100%;
  }
  .band--red  { fill: var(--brand-red); }
  .band--blue { fill: var(--brand-blue); }

  .brand-name {
    position: absolute;
    font-family: "PT Sans Narrow", "Arial Narrow", sans-serif;
    font-weight: 700;
    color: var(--brand-blue);
    letter-spacing: 0.5px;
    line-height: 1;
    display: flex;
    align-items: center;
    gap: 12px;
  }
  .brand-name__dot {
    width: 14px;
    height: 14px;
    border-radius: 50%;
    background: var(--brand-red);
  }
  .card--front .brand-name { left: 112px; top: 68px; font-size: 68px; }
  .card--back .brand-name  { left: 98px;  top: 126px; font-size: 68px; }

  .contact {
    position: absolute;
    font-family: "Open Sans", Arial, sans-serif;
    color: var(--text-light);
  }
  .person {
    right: 341px;
    top: 254px;
    text-align: right;
  }
  .person__name  { font-size: 17px; font-weight: 600; line-height: 22px; }
  .person__title { font-size: 14px; line-height: 20px; }

  .address {
    left: 239px;
    top: 220px;
    font-size: 14.5px;
    line-height: 21px;
    font-style: normal;
  }
  .address__company { font-size: 16px; font-weight: 700; }
</style>
</head>
<body>
<main class="canvas">

  <section class="card card--front" aria-label="Business card front">
    <svg class="card__bands" viewBox="0 0 555 343" preserveAspectRatio="none" aria-hidden="true">
      <path class="band--red" d="M0,118 C18,160 150,188 555,180 L555,186 C260,198 70,192 0,170 Z"/>
      <path class="band--blue" d="M0,176 C90,200 260,202 555,191 L555,343 L0,343 Z"/>
    </svg>

    <div class="brand-name">VorlexIT<span class="brand-name__dot"></span></div>

    <div class="contact person">
      <p class="person__name">Rashid Nawfal</p>
      <p class="person__title">Managing Director</p>
    </div>

    <address class="contact address">
      <p class="address__company">Vorlex IT</p>
      <p>Sdn. Bhd.3rd Floor, Block C,</p>
      <p>Wisma LPN,No.14 Jalan Seri Hamzani,</p>
      <p>58410, Kuala Lumpur</p>
      <p>Malaysia</p>
    </address>
  </section>

  <section class="card card--back" aria-label="Business card back">
    <div class="brand-name">VorlexIT<span class="brand-name__dot"></span></div>
  </section>

</main>
</body>
</html>
```